Venture Capital Firm Needs Website Redesign

We need a bold revamp of our website (https://halvenmoor.vc/)
which at the moment looks washed out. We want a crisp, fresh and unique look. Feel free to keep as much or as little content in the site. The only thing we need to keep is a team section. The site should convey a clear distinction between our 3 product lines: Venture Capital, Private Credit, and Crypto. Two versions of our logo are attached and they should not change. For design inspirations, we like http://www.plumridgecap.com/ for a more simple site and for a more built out site we like http://tallowgate.com/

Updates
Industry/Entity Type
Investment
Coding
Coded - Design and coding required
Number of Pages Required
1 page
Font styles to use
Colors
Designer to choose colors to be used in the design.
Requirements
Must have
- - Clear distinction between our 3 product lines: Venture Capital, Private Credit
- - Team section

Nice to have
- Some really creative aspect like http://www.plumridgecap.com/ has with the distinction between first, second, and third kind

```html
<!DOCTYPE html>
<html lang="en">
<head>
<meta charset="utf-8">
<title>Halvenmoor</title>
<link href="https://fonts.googleapis.com/css2?family=Barlow:wght@400;500;600&family=Arimo:wght@400&display=swap" rel="stylesheet">
<style>
:root{
  --green:#7b925f;
  --green-soft:#eef1e9;
  --ink:#1f1f1f;
  --text:#3a3a3a;
  --footer:#ececec;
  --white:#ffffff;
}
*{margin:0;padding:0;box-sizing:border-box}
html,body{width:762px;height:1200px;overflow:hidden;background:var(--white)}
body{position:relative;font-family:"Barlow",Arial,sans-serif;color:var(--ink)}
.abs{position:absolute}

/* header */
.site-header{left:0;top:0;width:762px;height:56px;background:var(--white)}
.brand{left:62px;top:10px;display:flex;align-items:center;gap:7px}
.brand-mark{width:42px;height:42px;border:1.5px solid var(--ink);border-radius:50%}
.brand-name{font-weight:400;font-size:26px;letter-spacing:1px;color:var(--green)}
.main-nav{left:315px;top:29px;display:flex;gap:18px;font-size:10.3px;font-weight:400}
.main-nav a{color:var(--ink);text-decoration:none}
.main-nav a.active{color:var(--green);border-bottom:1px solid var(--green);padding-bottom:2px}

/* hero */
.hero{left:0;top:56px;width:762px;height:289px;background:radial-gradient(ellipse at 50% 50%,#fbfbfc 0%,#eceef2 60%,#dfe2e8 100%)}
.hero-title{left:0;top:152px;width:762px;text-align:center;font-size:24.5px;font-weight:500;line-height:32px;color:var(--ink);text-shadow:0 1px 2px rgba(0,0,0,.15)}
.btn{display:inline-block;background:var(--green);color:var(--white);border-radius:10px;font-size:10px;text-align:center;line-height:17px;text-decoration:none}
.hero-btn{left:339px;top:226px;width:81px}
.hero-arrow{top:192px;width:19px;height:17px;background:#2e2e2e;color:var(--white);font-size:11px;text-align:center;line-height:17px}
.hero-arrow.prev{left:4px;border-radius:0 3px 3px 0}
.hero-arrow.next{left:735px;border-radius:3px 0 0 3px}

/* services */
.service{top:377px;width:190px;text-align:center}
.service-icon{display:block;margin:0 auto}
.service h3{font-size:13.5px;font-weight:500;margin-top:6px}
.service p{font-family:"Arimo",Arial,sans-serif;font-size:7.4px;line-height:12.5px;color:var(--text);margin:3px auto 0;width:175px}
.service .read{display:inline-block;margin-top:7px;font-family:"Arimo",Arial,sans-serif;font-size:8.2px;color:var(--ink);text-decoration:underline}

/* team */
.team{left:0;top:566px;width:762px;height:215px;background:linear-gradient(90deg,#ece9e6,#f2efec 30%,#eae7e5 60%,#f1eeeb)}
.team-copy{left:0;top:608px;width:762px;text-align:center}
.team-copy h2{font-size:21px;font-weight:500}
.team-copy .lead{font-size:14.5px;line-height:22px;margin-top:4px;font-weight:500}
.team-copy .values{font-size:15px;letter-spacing:.3px;margin-top:5px;font-weight:500;word-spacing:10px}
.team-btn{left:340px;top:723px;width:82px;border-radius:10px 10px 0 0}

/* about */
.about{left:76px;top:803px;width:610px;text-align:center}
.about h2{font-size:21px;font-weight:500}
.about p{font-family:"Arimo",Arial,sans-serif;font-size:9.2px;line-height:17.6px;color:var(--text);margin-top:12px}
.about-btn{left:341px;top:926px;width:81px}

/* footer */
.site-footer{left:0;top:988px;width:762px;height:187px;background:var(--footer)}
.foot-col{top:1006px}
.foot-col h4{font-size:11.5px;font-weight:500;color:var(--ink)}
.foot-col h4::after{content:"";display:block;width:19px;height:1px;background:var(--green);margin-top:7px}
.quick-links{left:64px}
.quick-links ul{list-style:none;margin-top:7px}
.quick-links li{font-size:9px;font-weight:500;line-height:19.8px}
.newsletter{left:196px}
.newsletter p{font-size:7.8px;line-height:13px;margin-top:8px;width:145px;font-weight:400}
.email-field{width:153px;height:24px;border:1px solid #c9c9c9;background:var(--white);font-size:8px;line-height:22px;padding-left:10px;margin-top:13px;color:#444}
.subscribe{width:66px;height:24px;background:var(--green);color:var(--white);font-size:10px;line-height:24px;text-align:center;margin-top:15px}
.contact{left:392px;top:1011px}
.contact .org{font-size:11px;font-weight:600;margin-top:11px;margin-left:4px}
.contact .addr{font-size:7.8px;line-height:12.5px;margin-top:4px;margin-left:3px}
.contact .row{display:flex;align-items:center;gap:9px;font-size:7.8px;margin-top:6px;margin-left:3px}
.socials{display:flex;gap:8px;margin-top:11px}
.socials span{width:18px;height:18px;border:1px solid #555;border-radius:50%}
.foot-brand{left:569px;top:1018px;width:126px;text-align:center}
.foot-brand .ring{width:84px;height:84px;border:1.5px solid var(--ink);border-radius:50%;margin:0 auto}
.foot-brand .name{font-size:20px;font-weight:400;color:var(--green);letter-spacing:1px;margin-top:6px}
.copyright{left:0;top:1175px;width:762px;height:25px;background:var(--green);color:var(--white);font-size:8.5px;text-align:center;line-height:25px}
</style>
</head>
<body>

<header class="site-header abs">
  <div class="brand abs"><span class="brand-mark"></span><span class="brand-name">HALVENMOOR</span></div>
  <nav class="main-nav abs">
    <a class="active" href="#">Home</a><a href="#">Venture Capital</a><a href="#">Private Credit</a><a href="#">Crypto</a><a href="#">Team</a><a href="#">Blog</a><a href="#">Contact Us</a>
  </nav>
</header>

<section class="hero abs" role="img" aria-label="Light grey background with a faint network of connected nodes"></section>
<h1 class="hero-title abs">Halvenmoor Operates At The Intersection of Technology<br>And Novel Asset Classes.</h1>
<a class="btn hero-btn abs" href="#">Learn More</a>
<div class="hero-arrow prev abs">&#8249;</div>
<div class="hero-arrow next abs">&#8250;</div>

<section class="service abs" style="left:74px">
  <svg class="service-icon" width="76" height="76" viewBox="0 0 76 76">
    <rect x="6" y="6" width="64" height="64" rx="10" fill="#eef1e9"/>
    <path d="M22 52 l12 -12 8 8 14 -16" fill="none" stroke="#7b925f" stroke-width="2"/>
    <path d="M48 32 h8 v8" fill="none" stroke="#7b925f" stroke-width="2"/>
  </svg>
  <h3>Venture Capital</h3>
  <p>We invest in early-stage startups led by founders who are passionate and knowledgeable...[+]</p>
  <a class="read" href="#">Read More</a>
</section>

<section class="service abs" style="left:286px">
  <svg class="service-icon" width="76" height="76" viewBox="0 0 76 76">
    <rect x="6" y="6" width="64" height="64" rx="10" fill="#eef1e9"/>
    <rect x="20" y="27" width="36" height="23" rx="3" fill="none" stroke="#7b925f" stroke-width="2"/>
    <line x1="20" y1="33" x2="56" y2="33" stroke="#7b925f" stroke-width="2"/>
    <line x1="25" y1="43" x2="35" y2="43" stroke="#7b925f" stroke-width="2"/>
  </svg>
  <h3 style="margin-top:11px">Private Credit</h3>
  <p>Halvenmoor Private Credit provides capital to lending businesses that are focused on using technology..[+]</p>
  <a class="read" href="#">Read More</a>
</section>

<section class="service abs" style="left:498px">
  <svg class="service-icon" width="76" height="76" viewBox="0 0 76 76">
    <rect x="6" y="6" width="64" height="64" rx="10" fill="#eef1e9"/>
    <rect x="22" y="40" width="7" height="13" fill="#7b925f"/>
    <rect x="34" y="32" width="7" height="21" fill="#7b925f"/>
    <rect x="46" y="24" width="7" height="29" fill="#7b925f"/>
  </svg>
  <h3 style="margin-top:11px">Crypto</h3>
  <p>The Halvenmoor Crypto Index tracks the top 15 crypto currencies weighted by market cap &amp; rebalanced...[+]</p>
  <a class="read" href="#">Read More</a>
</section>

<section class="team abs" role="img" aria-label="Faded grid of team member portrait photos"></section>
<div class="team-copy abs">
  <h2>Our Team</h2>
  <p class="lead">Our Highly Skilled Financial Consultants Are People Who Personifies The Very Qualities<br>That Have Made Us Successful</p>
  <p class="values">KNOWLEDGE. EXPERIENCE. ENTHUSIAM. DEDICATION</p>
</div>
<a class="btn team-btn abs" href="#">Read More</a>

<section class="about abs">
  <h2>About Us</h2>
  <p>Halvenmoor operates three businesses that bridge technology and finance. We invest in pre-seed venture capital, and build software for the companies we invest in. We manage direct private credit funds that provide private credit capital to alternative private credit platforms, enabling them to finance the loans they originate. We create crypto funds for individuals, IRAs and institutions to get simple and easy access to cryptocurrencies.</p>
</section>
<a class="btn about-btn abs" href="#">Call Us Today</a>

<footer class="site-footer abs"></footer>
<div class="foot-col quick-links abs">
  <h4>Quick Links</h4>
  <ul><li>Home</li><li>Venture Capital</li><li>Private Credit</li><li>Crypto</li><li>Team</li><li>Blog</li></ul>
</div>
<div class="foot-col newsletter abs">
  <h4>Newsletter Signup</h4>
  <p>Lorem ipsum dolor sit amet, sectetuer adipiscing elit, sed diam nonummy nibh euismod tincidunt.</p>
  <div class="email-field">Enter Your Email Here</div>
  <div class="subscribe">Subscribe</div>
</div>
<div class="foot-col contact abs">
  <h4>Contact Details</h4>
  <div class="org">Halvenmoor</div>
  <div class="addr">218 Larkspur Avenue, Suite 4<br>Easton Ridge, NY 10417</div>
  <div class="row">
    <svg width="9" height="9" viewBox="0 0 10 10"><path d="M2 1 l2 2 -1 1.5 c.8 1.4 1.7 2.3 3 3 l1.5 -1 2 2 -1.5 1.5 C4 9 1 6 .5 2.5z" fill="#7b925f"/></svg>
    <span>555-014-2268</span>
  </div>
  <div class="row">
    <svg width="10" height="8" viewBox="0 0 10 8"><rect x=".5" y=".5" width="9" height="7" fill="none" stroke="#7b925f"/><path d="M.5 .5 l4.5 4 4.5-4" fill="none" stroke="#7b925f"/></svg>
    <span>info@halvenmoor.vc</span>
  </div>
  <div class="socials"><span></span><span></span><span></span><span></span></div>
</div>
<div class="foot-brand abs">
  <div class="ring"></div>
  <div class="name">HALVENMOOR</div>
</div>
<div class="copyright abs">Copyright © 2018 Halvenmoor . All Rights Reserved</div>

</body>
</html>
```